Creative Web Design for an ERP (technology) Consulting Business

I need two pages designed for the ERP Project Management Consulting Company I am starting. One page is the home page, the other page is an important inside page.

I've looked at many different templates for sites like this, and they all look the same to me. I am working with Drafthollow designers because I want something unique.

This site will be implemented with Wordpress using the Elementor framework,

About Me ---
I have worked with Drafthollow several times before, and I have tired to do everything I can to ve helpful. In the uploads, you will find PDF's with wireframes outlning the layout of the pages, as well as explanatios for each section. There are Word documents that you can copy into text. The list below explains the files included.

Although the wireframes suggest a layout, please feel free to use your creativity - often, I find that the designs I like the most are designs I have never thought of.

About the Company --
ERP (Enterprise Resource Planning) systems are business computer systems that tie different businesss functions together. These systems are expensive and complicated, and efforts to implement them often fail. The purpose of the company is to increase the chance of success by focusing on the things that need to be right.

I have uploaded several files to help clarify what I am looking for:
• 1a - Home Page Wireframe - PDF
Wireframe for the home page with an explanation of each section.
• 1b - Home Page Text – Word
A Word document so that you can copy the text.
• 2 - Silver Kestrel Logo – ZIP
Four different versions of the company logo in Adobe Illustrator, PNG, and JPG formats. Any of the four are acceptable:
1. Logo_1 – Black on Transparent – Same Line ERP
2. Logo_2 – White on Transparent – Same Line ERP
3. Logo_3 – Black on Transparent – Big ERP on Different Line
4. Logo_4 – White on Transparent – Big ERP on Different Line
• 3a - Silver Kestrel Page Wireframe – PDF
Wireframe for he Silver Kestrel page, with explanations and a detailed breakdown of the top section.
• 3b - Silver Kestrel Text – Word
• 4 - Colors and Palettes – PDF
• 5 - Change Management Icon – EPS
• 6 – Site Map
If you wish to see it, the site map provides an idea of the entire site. The two pages circled in red are the ones I need to be designed.

Thank you for your interest in this project!

Target Market(s)

Corporate decision makers, primarily CIOs and CFOs, as well as ERP project managers and influencers.

Industry/Entity Type

Consulting

Number of Pages Required

2 page

Font styles to use
Sans Serif

Requirements
Must have
• Pages that contain the elements explained on the wireframes provided.
Nice to have
• A design that looks and feels unique
Should not have
• A typical, template layour

```html
<!DOCTYPE html>
<html lang="en">
<head>
<meta charset="utf-8">
<title>Silver Kestrel — Adaptive 8 Method</title>
<link href="https://fonts.googleapis.com/css2?family=Inter:wght@400;500;600;700&display=swap" rel="stylesheet">
<style>
  :root{
    --bg:#eceef3;
    --ink:#1d1f24;
    --muted:#4a4d55;
    --line:#c9ccd3;
    --red:#e0573f;
    --orange:#d9843f;
    --yellow:#d7b234;
    --green:#4f9a55;
    --teal:#2b8a86;
    --pink:#d24468;
    --purple:#5f4f9f;
    --blue:#3f6ba8;
    --indigo:#544b98;
    --label-teal:#2a8c8a;
    --label-blue:#3a6ea7;
  }
  *{box-sizing:border-box;margin:0;padding:0}
  html,body{width:673px;height:1200px;overflow:hidden}
  body{
    font-family:"Inter",Arial,sans-serif;color:var(--ink);
    background:radial-gradient(circle at 50% 50%,#f8f9fb 0%,var(--bg) 60%);
    position:relative;
  }
  .abs{position:absolute}
  /* header */
  .brand{left:23px;top:17px;display:flex;align-items:center;gap:7px;font-weight:700;font-size:17px}
  .brand-dot{width:14px;height:14px;border-radius:50%;background:var(--red)}
  .nav-item{top:22px;font-size:9px;font-weight:500;letter-spacing:.3px;white-space:nowrap}
  .nav-cta{left:568px;top:11px;width:84px;height:31px;border:1px solid var(--line);border-radius:16px;background:#fff;
    font-size:9.5px;font-weight:600;display:flex;align-items:center;justify-content:center}
  .rule{left:21px;width:631px;height:1px;background:var(--line)}
  /* hero */
  .hero-title{left:33px;top:128px;font-size:36px;font-weight:500;line-height:46px}
  .hero-sub{left:30px;top:241px;font-size:14.5px;line-height:22px;color:var(--ink)}
  .spine{left:338px;top:130px;width:1px;height:234px;background:#9aa3a9}
  .spine-dot{left:334px;top:360px;width:8px;height:8px;border-radius:50%;background:#7fa3a2}
  .kicker{left:402px;top:141px;font-size:16px;font-weight:500;letter-spacing:.2px}
  .kicker em{font-style:normal;color:var(--orange)}
  .kicker-line{left:402px;top:176px;width:114px;height:2px;background:var(--ink)}
  .intro{left:402px;top:196px;font-size:14.5px;line-height:20px}
  .intro em{font-style:normal;color:var(--orange)}
  .btn{left:401px;top:272px;width:120px;height:39px;border-radius:20px;background:var(--red);color:#fff;
    font-size:10px;font-weight:600;letter-spacing:.8px;display:flex;align-items:center;justify-content:center;
    box-shadow:0 4px 10px rgba(224,87,63,.25)}
  /* diagram */
  .tile{width:64px;height:64px;border-radius:10px;display:flex;align-items:center;justify-content:center;
    box-shadow:0 3px 8px rgba(0,0,0,.12)}
  .tile svg{width:28px;height:28px}
  .diamond{transform:rotate(45deg);width:50px;height:50px;border-radius:8px}
  .diamond svg{transform:rotate(-45deg);width:24px;height:24px}
  .hub{left:302px;top:561px;width:68px;height:66px;border-radius:12px;background:#fff;display:flex;align-items:center;justify-content:center;box-shadow:0 2px 10px rgba(0,0,0,.06)}
  .node{width:7px;height:7px;border-radius:50%}
  .label h3{font-size:14.5px;font-weight:600;margin-bottom:4px}
  .label p{font-size:11.5px;line-height:15px}
  .right{text-align:right}
  .center{text-align:center}
  .connector{position:absolute;left:0;top:0}
  /* success */
  .section-title{left:0;width:673px;top:866px;text-align:center;font-size:17px;font-weight:500;letter-spacing:.5px}
  .section-text{left:0;width:673px;top:898px;text-align:center;font-size:15.5px;line-height:23px}
  .col-rule{top:978px;width:1px;height:206px;background:var(--line)}
  .step{top:1012px;width:150px}
  .step-label{font-size:8.5px;font-weight:500;letter-spacing:.5px;margin-bottom:27px}
  .step h4{font-size:13px;font-weight:600;line-height:17px;margin-bottom:5px}
  .step p{font-size:9.5px;line-height:13px;color:var(--muted)}
</style>
</head>
<body>
  <header>
    <div class="abs brand"><span class="brand-dot"></span>Silver Kestrel</div>
    <nav>
      <span class="abs nav-item" style="left:273px">METHOD ▾</span>
      <span class="abs nav-item" style="left:341px">ABOUT</span>
      <span class="abs nav-item" style="left:400px">PILLARS</span>
      <span class="abs nav-item" style="left:452px">PROJECT</span>
      <span class="abs nav-item" style="left:515px">BLOG</span>
    </nav>
    <div class="abs nav-cta">CONTACT US</div>
  </header>
  <div class="abs rule" style="top:53px"></div>

  <section class="hero">
    <h1 class="abs hero-title">Adaptive 8<br>Method</h1>
    <p class="abs hero-sub">Framework grouping eight critical<br>success factors into high-level categories<br>for ERP project success.</p>
    <div class="abs spine"></div>
    <div class="abs spine-dot"></div>
    <h2 class="abs kicker">PROVEN THE<em>ORY. PILLARS</em></h2>
    <div class="abs kicker-line"></div>
    <p class="abs intro">A framework aligning projects<br>into their natural phases that<br><em>drive results.</em></p>
    <a class="abs btn">LEARN MORE</a>
  </section>

  <section class="diagram">
    <svg class="connector" width="673" height="820" aria-hidden="true">
      <g stroke="#a9aeb6" stroke-width="1">
        <line x1="337" y1="455" x2="337" y2="466"/>
        <line x1="218" y1="487" x2="248" y2="512"/>
        <line x1="457" y1="487" x2="428" y2="512"/>
        <line x1="188" y1="594" x2="200" y2="594"/>
        <line x1="486" y1="594" x2="474" y2="594"/>
        <line x1="218" y1="702" x2="248" y2="675"/>
        <line x1="455" y1="702" x2="426" y2="675"/>
      </g>
    </svg>
    <div class="abs node" style="left:334px;top:452px;background:var(--yellow)"></div>
    <div class="abs node" style="left:215px;top:484px;background:var(--orange)"></div>
    <div class="abs node" style="left:454px;top:484px;background:var(--green)"></div>
    <div class="abs node" style="left:185px;top:591px;background:var(--pink)"></div>
    <div class="abs node" style="left:483px;top:591px;background:var(--teal)"></div>
    <div class="abs node" style="left:215px;top:699px;background:var(--purple)"></div>
    <div class="abs node" style="left:452px;top:699px;background:var(--blue)"></div>

    <div class="abs tile" style="left:244px;top:509px;background:var(--orange)">
      <svg viewBox="0 0 28 28" fill="none" stroke="#fff" stroke-width="1.6"><rect x="4" y="6" width="20" height="14" rx="1"/><path d="M4 11h20M10 6v14M16 6v14M8 24h12"/></svg>
    </div>
    <div class="abs tile" style="left:361px;top:509px;background:var(--green)">
      <svg viewBox="0 0 28 28" fill="none" stroke="#fff" stroke-width="1.6"><path d="M5 22l7-9 5 5 6-11"/><rect x="17" y="4" width="6" height="6"/></svg>
    </div>
    <div class="abs tile" style="left:247px;top:612px;background:var(--purple)">
      <svg viewBox="0 0 28 28" fill="none" stroke="#fff" stroke-width="1.6"><circle cx="14" cy="14" r="9"/><path d="M5 14h18M14 5c4 4 4 14 0 18M14 5c-4 4-4 14 0 18"/></svg>
    </div>
    <div class="abs tile" style="left:361px;top:612px;background:var(--blue)">
      <svg viewBox="0 0 28 28" fill="none" stroke="#fff" stroke-width="1.6"><path d="M14 4v20M8 10l6-6 6 6M8 18h12"/></svg>
    </div>
    <div class="abs tile diamond" style="left:312px;top:469px;background:var(--yellow)">
      <svg viewBox="0 0 28 28" fill="none" stroke="#fff" stroke-width="1.8"><path d="M6 12l8-6 8 6v10H6z"/></svg>
    </div>
    <div class="abs tile diamond" style="left:203px;top:569px;background:var(--pink)">
      <svg viewBox="0 0 28 28" fill="none" stroke="#fff" stroke-width="1.8"><path d="M7 6h14L7 22h14z"/></svg>
    </div>
    <div class="abs tile diamond" style="left:421px;top:569px;background:var(--teal)">
      <svg viewBox="0 0 28 28" fill="none" stroke="#fff" stroke-width="1.8"><rect x="6" y="6" width="16" height="16" rx="2"/><path d="M10 17v-6h8"/></svg>
    </div>
    <div class="abs tile diamond" style="left:311px;top:671px;background:var(--indigo)">
      <svg viewBox="0 0 28 28" fill="none" stroke="#fff" stroke-width="1.8"><rect x="7" y="5" width="14" height="18" rx="2"/><path d="M11 10h6M11 14h6M11 18h3"/></svg>
    </div>
    <div class="abs hub">
      <svg width="34" height="30" viewBox="0 0 34 30" fill="none" stroke="var(--green)" stroke-width="2"><rect x="2" y="2" width="30" height="26" rx="2"/><path d="M2 9h30M2 16h30M2 23h30M12 9v7M22 16v7"/></svg>
    </div>

    <div class="abs label center" style="left:237px;top:385px;width:200px">
      <h3>Pillar 1</h3>
      <p style="color:var(--orange)">Data management<br>and governance</p>
    </div>
    <div class="abs label right" style="left:40px;top:461px;width:156px">
      <h3>Strategic</h3>
      <p style="color:var(--label-teal)">Project alignment</p>
    </div>
    <div class="abs label right" style="left:10px;top:576px;width:155px">
      <h3>Project 12</h3>
      <p style="color:var(--red)">Business process<br>process integration</p>
    </div>
    <div class="abs label" style="left:78px;top:683px;width:150px">
      <h3 style="color:#3c2a6a">Pillars 23</h3>
      <p style="color:var(--red)">System and change<br>iteration</p>
    </div>
    <div class="abs label center" style="left:237px;top:738px;width:200px">
      <h3>System</h3>
      <p style="color:var(--label-blue)">Smart profile<br>database<br>method</p>
    </div>
    <div class="abs label" style="left:481px;top:461px;width:190px">
      <h3>Pillar 3 21</h3>
      <p style="color:var(--label-teal)">Data and integration<br>method support</p>
    </div>
    <div class="abs label" style="left:510px;top:576px;width:160px">
      <h3>Pillar 45</h3>
      <p style="color:var(--label-teal)">Training and<br>mindset of teams</p>
    </div>
    <div class="abs label" style="left:481px;top:683px;width:190px">
      <h3>Pillar 52</h3>
      <p style="color:var(--label-blue)">Post implementation change<br>management</p>
    </div>
  </section>

  <section class="success">
    <h2 class="abs section-title">SUCCESS</h2>
    <p class="abs section-text">A framework of critical pillars grouping core areas,<br>enabling stakeholders across all 8 project phases.</p>
    <div class="abs rule" style="top:960px"></div>
    <div class="abs col-rule" style="left:174px"></div>
    <div class="abs col-rule" style="left:336px"></div>
    <div class="abs col-rule" style="left:500px"></div>

    <div class="abs step" style="left:29px">
      <div class="step-label">STEP 1</div>
      <h4>Training and<br>Motivation</h4>
      <p>Our coaches help every<br>team build confidence with<br>the new tools each day.</p>
    </div>
    <div class="abs step" style="left:186px">
      <div class="step-label">STEP 2</div>
      <h4>Project Action,<br>Method Pillars</h4>
      <p>Clear roles and a shared<br>plan keep the project on<br>track from day one.</p>
    </div>
    <div class="abs step" style="left:348px">
      <div class="step-label">STEP 3</div>
      <h4>Lean Method<br>Method Pathing</h4>
      <p>Processes are reviewed<br>and refined before the<br>system goes live for<br>each user group.</p>
    </div>
    <div class="abs step" style="left:513px">
      <div class="step-label">STEP 4</div>
      <h4>Post Implementation<br>Support</h4>
      <p>Lasting support after the<br>launch keeps gains and<br>results on course.</p>
    </div>
  </section>
</body>
</html>
```